CREATIVE DESIGNERS NEEDED & Enhance Your Business Card Portfolio

Artistic, unique, professional real estate card needed - see attached documents "B-cards.pdf" for all details and examples.True Designers will see other projects of ours come online here. We like long-term relationships for creative designers. This business card will be used in two U.S. states and is central to our business and other future marketing.

Target Market(s)

Buyers and Sellers of real estate

Industry/Entity Type

Real Estate Agent

Contact Information for Business Card

See attached detailed brief

Other font styles liked:
• ADAM.CG PRO & NewsGoth BT

Requirements
Must have
• 2-sided, creative (non-traditional layout/design). Incorporate a cut-out (for texture, and make it fun! No boring templates for this card -
Nice to have
• See attached detailed brief
Should not have

```html
<!DOCTYPE html>
<html lang="en">
<head>
<meta charset="utf-8">
<title>Dana Hollis Group Real Estate – Business Card</title>
<link href="https://fonts.googleapis.com/css2?family=Josefin+Sans:wght@400;600&family=Open+Sans:wght@400;700&family=Libre+Baskerville&display=swap" rel="stylesheet">
<style>
  :root {
    --bg: #2b2d31;
    --slate: #3e4a5a;
    --slate-light: #4b5869;
    --white: #ffffff;
    --paper: #f6f6f6;
    --ink: #3a4250;
    --red: #c8322f;
    --grey: #9a9ea5;
  }
  * { box-sizing: border-box; margin: 0; padding: 0; }
  html, body { width: 1200px; height: 900px; overflow: hidden; }
  body {
    background: var(--bg);
    display: flex;
    flex-direction: column;
    align-items: center;
    justify-content: center;
    gap: 40px;
  }
  .card {
    width: 620px;
    height: 354px;
    position: relative;
    overflow: hidden;
    box-shadow: 0 12px 30px rgba(0,0,0,.45);
  }
  /* Front */
  .card-front {
    background: linear-gradient(135deg, var(--slate-light), var(--slate));
    display: flex;
    align-items: center;
    justify-content: center;
  }
  .brand {
    display: flex;
    align-items: center;
    gap: 16px;
  }
  .brand-mark {
    width: 22px; height: 22px;
    background: var(--red);
  }
  .brand-name {
    font-family: "Josefin Sans", sans-serif;
    font-weight: 600;
    line-height: 1.1;
    letter-spacing: 2px;
    text-transform: uppercase;
  }
  .card-front .brand-name { color: var(--white); font-size: 30px; }
  /* Back */
  .card-back { background: var(--paper); }
  .photo {
    position: absolute;
    right: 0; top: 0;
    width: 250px; height: 100%;
    background: linear-gradient(160deg, #d9d9d9 0%, #8c8f94 55%, #5d6066 100%);
  }
  .back-content {
    position: absolute;
    left: 40px; top: 46px;
    width: 330px;
  }
  .card-back .brand-name { color: var(--ink); font-size: 22px; }
  .region {
    font-family: "Libre Baskerville", serif;
    font-size: 11px;
    color: var(--grey);
    margin: 6px 0 0 38px;
  }
  .tagline {
    font-family: "Libre Baskerville", serif;
    font-size: 12px;
    color: var(--red);
    margin-top: 34px;
  }
  .agent {
    font-family: "Open Sans", sans-serif;
    color: var(--ink);
    margin-top: 14px;
    font-size: 20px;
  }
  .agent strong { font-weight: 700; }
  .agent .title { font-size: 13px; margin-left: 4px; }
  .rule { height: 2px; background: var(--red); margin: 8px 0; }
  .phones {
    display: flex;
    justify-content: space-between;
    font-family: "Open Sans", sans-serif;
    font-size: 14px;
    color: var(--red);
  }
  .phone { display: flex; align-items: center; gap: 6px; }
  .badges { display: flex; gap: 8px; margin-top: 22px; }
  .badge { width: 34px; height: 34px; border: 2px solid var(--ink); }
  .badge.wide { width: 60px; }
</style>
</head>
<body>
  <section class="card card-front">
    <div class="brand">
      <span class="brand-mark"></span>
      <span class="brand-name">Dana Hollis Group<br>Real Estate</span>
    </div>
  </section>

  <section class="card card-back">
    <div class="photo" role="img" aria-label="Black and white portrait photo of the agent"></div>
    <div class="back-content">
      <div class="brand">
        <span class="brand-mark"></span>
        <span class="brand-name">Dana Hollis Group<br>Real Estate</span>
      </div>
      <p class="region">San Diego &amp; Phoenix</p>
      <p class="tagline">Residential. Investment. Development</p>
      <p class="agent">Dana <strong>Hollis</strong><span class="title">Broker Associate &amp; Realtor</span></p>
      <div class="rule"></div>
      <div class="phones">
        <span class="phone">
          <svg width="14" height="12" viewBox="0 0 14 12" aria-hidden="true"><path d="M1 4 Q7 -1 13 4 L11 6 L9 4.5 L5 4.5 L3 6 Z M3 6 L11 6 L12 11 L2 11 Z" fill="currentColor"/></svg>
          (555) 010-7355
        </span>
        <span class="phone">
          (555) 014-2280
          <svg width="9" height="14" viewBox="0 0 9 14" aria-hidden="true"><rect x="1" y="1" width="7" height="12" rx="1.5" fill="none" stroke="currentColor" stroke-width="1.5"/></svg>
        </span>
      </div>
      <div class="badges">
        <span class="badge"></span>
        <span class="badge wide"></span>
      </div>
    </div>
  </section>
</body>
</html>
```